Larkfield Clinic Booklet 2016

Larkfield Clinic is a multi-specialty Practice in Midtown Manhattan offering advanced care in multiple areas of medicine. See our table of contents (PDF Uploaded)
Our designed booklet should be clean, easy to read, contemporary, high-end and elegant.
We need a general theme, Layout for cover and templates for internal.
We are entertaining the idea of two different sizes
8 x 10
or
11 x 8.5
Our tagline " The Future of Medicine is Here"
We will provide all the text content
The link to our website
www.LarkfieldCL.example
Uploaded files are as follows.. Logo, Our Team Photo and the PDF listing the table of contents.

```html
<!DOCTYPE html>
<html lang="en">
<head>
<meta charset="utf-8">
<title>Larkfield Clinic Booklet – Pages 9–10</title>
<link rel="stylesheet" href="https://fonts.googleapis.com/css2?family=Mulish:wght@400;500&family=Roboto:wght@400;700&display=swap">
<style>
  :root{
    --navy:#0b0c52;
    --orange:#e5960f;
    --pill:#e4e4e6;
    --ink:#3b3b3b;
    --paper:#ffffff;
    --photo-light:#eef0f2;
    --photo-mid:#c9ced4;
    --photo-dark:#5f6670;
  }
  *{margin:0;padding:0;box-sizing:border-box}
  html,body{width:1200px;height:1000px;overflow:hidden;background:#fff}
  .canvas{position:relative;width:1200px;height:1000px;background:#fff}
  .spread{position:absolute;left:14px;top:270px;width:1174px;height:458px;background:var(--paper);
    box-shadow:0 2px 6px rgba(0,0,0,.35);overflow:hidden}
  .page{position:absolute;top:0;height:458px;width:587px;overflow:hidden}
  .page--left{left:0}
  .page--right{left:587px}

  .side-tab{position:absolute;top:182px;width:92px;height:92px;border-radius:50%;background:var(--navy)}
  .page--left .side-tab{left:-46px}
  .page--right .side-tab{right:-46px}

  .title-pill{position:absolute;background:var(--pill);font-family:"Mulish",sans-serif;font-weight:400;
    color:var(--navy);font-size:19px;line-height:22px}
  .page--left .title-pill{left:0;top:18px;width:274px;height:50px;border-radius:0 25px 25px 0;padding:13px 0 0 61px}
  .page--right .title-pill{right:0;top:22px;width:276px;height:50px;border-radius:25px 0 0 25px;padding:2px 0 0 45px}

  .body{position:absolute;font-family:"Roboto",sans-serif;font-size:6.6px;line-height:9.6px;color:var(--ink)}
  .body p{margin-bottom:9px}
  .page--left .body{left:62px;top:79px;width:206px}
  .page--right .body{left:317px;top:79px;width:203px;text-align:justify}
  .body h2{font-family:"Mulish",sans-serif;font-weight:400;font-size:14px;color:var(--navy);margin:14px 0 8px;line-height:16px}
  .goals{list-style:none}
  .goals li{position:relative;padding-left:7px;line-height:11.5px}
  .goals li::before{content:"";position:absolute;left:0;top:2.5px;width:3.5px;height:7px;border-radius:0 4px 4px 0;background:var(--orange)}

  .tagline{position:absolute;font-family:"Roboto",sans-serif;font-weight:700;font-size:12px;color:var(--navy);letter-spacing:.1px}
  .page--left .tagline{left:60px;top:407px}
  .page--right .tagline{left:321px;top:412px}

  .photo{position:absolute;top:0;height:458px}
  .photo--rehab{left:281px;width:306px;
    background:linear-gradient(160deg,var(--photo-light) 0%,var(--photo-mid) 45%,var(--photo-dark) 100%);
    -webkit-mask-image:linear-gradient(90deg,transparent 0,#000 70px);mask-image:linear-gradient(90deg,transparent 0,#000 70px)}
  .photo--ultrasound{left:0;width:285px;
    background:linear-gradient(200deg,#f2ece9 0%,#d9dcdf 45%,#a9afb6 100%);
    -webkit-mask-image:linear-gradient(270deg,transparent 0,#000 80px);mask-image:linear-gradient(270deg,transparent 0,#000 80px)}
  .inset{position:absolute;border-radius:50%;border:3px solid #fff;background:linear-gradient(180deg,#f3f1f0,#cfd3d8)}
  .inset--one{left:371px;top:217px;width:136px;height:136px}
  .inset--two{left:296px;top:313px;width:136px;height:136px}

  .folio{position:absolute;top:14px;font-family:"Roboto",sans-serif;font-weight:700;font-size:19px}
  .folio--left{right:17px;color:var(--navy)}
  .folio--right{left:17px;color:var(--orange)}
</style>
</head>
<body>
<div class="canvas">
  <div class="spread">
    <section class="page page--left">
      <div class="photo photo--rehab" role="img" aria-label="Photo of a therapist guiding a patient on rehabilitation equipment"></div>
      <div class="inset inset--one" role="img" aria-label="Photo of a therapist treating a patient's knee"></div>
      <div class="inset inset--two" role="img" aria-label="Photo of a therapist assisting a patient with a balance exercise"></div>
      <span class="folio folio--left">9</span>
      <div class="side-tab"></div>
      <h1 class="title-pill">Physical Rehabilitation</h1>
      <div class="body">
        <p>Larkfield Clinic uses a comprehensive program to restore your natural motion, strength and well being. After an injury or chronic pain, your body loses key muscle strength and movement. Our physical therapy specialists are experts in helping you restore natural pain-free movements.</p>
        <h2>Methodology:</h2>
        <p>Physical therapy treatments utilize specific hands-on treatments, modalities, and gentle therapeutic exercises to help you recover from injury and feel your best.</p>
        <p>Our team works together to provide you with a unique and unparalleled treatment that achieves the highest results. If you have been recently injured or are suffering from long-standing pain, we can help you where others have not.</p>
        <h2>Goals of Physical Rehab:</h2>
        <ul class="goals">
          <li>Relieve Pain</li>
          <li>Increase Mobility</li>
          <li>Home Exercise Program</li>
          <li>Improve Function and Posture</li>
          <li>Correct Body Mechanics</li>
        </ul>
      </div>
      <p class="tagline">HEALTH IS THE GREATEST WEALTH</p>
    </section>

    <section class="page page--right">
      <div class="photo photo--ultrasound" role="img" aria-label="Photo of a patient lying down beside an ultrasound machine"></div>
      <span class="folio folio--right">10</span>
      <div class="side-tab"></div>
      <h1 class="title-pill">Advanced Testing:<br>Ultrasound</h1>
      <div class="body">
        <p>Ultrasound uses sound waves to detect areas of different density in the human body. Our advanced ultrasound equipment is used to detect areas in your body that are inflamed or under chronic stress.</p>
        <p>Ultrasound evaluation is used as a tool for our specialists to hone in on the areas that will result in the fastest recovery for you. As an example, being able to detect areas of specific inflammation in the joints of the spine, can assist our physicians, chiropractors and therapists when creating a treatment plan that will restore health to that area.</p>
        <h2>Methodology:</h2>
        <p>Ultrasound is non-invasive and no sensation is felt by the patient. After a thorough consultation with our doctors, ultrasound testing may be determined necessary to further detect the areas that will allow us to best restore your health.</p>
      </div>
      <p class="tagline">HEALTH IS THE GREATEST WEALTH</p>
    </section>
  </div>
</div>
</body>
</html>
```